BDW - Brochure Design Project

We need to update our marketing material with a new brochure for our company Brightmoor Data Works Inc..

Our company offerings are

Systems integration
IT Support
Nimbrel - Disaster Recovery solution - Nimbrel Information is in a attached document
Harbor Sky Suite - Hosted Mailvane and Cloud Servers
N.O.C. Managed Services
Around-the-clock network surveillance
Performance monitoring
Trouble ticket management
Event management
Guaranteed service levels (service assurance)

I'm uploading out old brochure. We think one with newer technology graphs and more bullet like instead of that much information would be better. suggestions are appreciated.
Updates

Based on some questions FYI
1) the old brochure is 4 years old so a in the experiance years is over 18 years
2) Also Please do not include the list of customers instead
    Some of our Customers includes:
     - Healthcare
     - Government
     - Educational Institutions
     - Banking & Insurance companies
     - Pharmaceutical, Bio-Technology and Medical Devices companies
     - Manufacturing and Regulatory Organizations
     - Many others

Hello everyone the fact  that I upload that brochure is to only to pick the content because that brochure have like 5 year old. We think one with newer technology graphs and more bullet like instead of that much information would be better of course verify the "Look and Feel" and the "requirement". On the file I upload too a Flyer, that flyer have the newer BDW Partners on the old brochure the only partners are Veltro, Dranwell, QZR Palvo, Membrix,XVL

remeber do not use the old brochure at reference is only to pick the content, create the brochure has you understand he be best and do not put the slogan that say (SIMPLIFYING IT). thank you all - any question let me know 

Target Market(s)

Our Services are IT so our audiance are both Executive and technical Persons

Industry/Entity Type

Marketing

Requirements
Must have
• 1) It must have our quote "A world class service with you in mind"
2) It must have the newer logo (uploaded) We are also putting a new Logo project as well but the current logo is attached
3) Partners logos - See BDW flyer PDF for the names
4)

```html
<!DOCTYPE html>
<html lang="en">
<head>
<meta charset="utf-8">
<title>BDW Brochure Spread</title>
<link rel="stylesheet" href="https://fonts.googleapis.com/css2?family=Arimo:ital,wght@0,400;0,700;1,400;1,700&family=Roboto+Condensed:wght@400;700&display=swap">
<style>
  :root {
    --amber: #e2a553;
    --ink: #1b1b1b;
    --green: #1f7a35;
    --green-light: #6aa532;
    --check-blue: #2b5fb3;
    --paper-light: #f7f7f7;
    --tile-blue: #3a8ee0;
    --tile-deep: #1c5fbf;
    --partner-grey: #5a5a5a;
  }
  * { box-sizing: border-box; margin: 0; padding: 0; }
  html, body { width: 1200px; height: 933px; overflow: hidden; background: #fff; }
  body { font-family: "Arimo", Arial, sans-serif; color: var(--ink); }

  .spread { position: relative; width: 1200px; height: 933px; overflow: hidden; }

  /* ---------- inside panel (left) ---------- */
  .panel-inside {
    position: absolute; left: 0; top: 0; width: 598px; height: 933px;
    background: linear-gradient(160deg, var(--paper-light) 0%, #e4e4e4 55%, #f2f2f2 100%);
  }
  .intro-band {
    position: absolute; left: 0; top: 46px; width: 596px; height: 112px;
    background: var(--amber);
    box-shadow: 0 3px 6px rgba(0,0,0,.25);
    padding: 16px 0 0 52px;
    font-size: 21px; line-height: 29px; color: #111;
  }
  .intro-band .brand { font-weight: 700; font-style: italic; }

  .section-label {
    position: absolute; left: 36px; width: 299px; height: 29px;
    background: var(--amber);
    font-weight: 700; line-height: 29px; padding-left: 7px;
  }
  .label-offerings { top: 172px; font-size: 15.5px; }
  .label-customers { top: 432px; font-size: 17px; }

  .offerings {
    position: absolute; left: 44px; top: 206px; list-style: none;
    font-size: 14.5px; line-height: 21.8px;
  }
  .offerings li::before { content: "• "; }
  .offerings .note { font-style: italic; font-size: 13.5px; }

  .customers {
    position: absolute; left: 41px; top: 470px; list-style: none;
    font-size: 16.5px; letter-spacing: .2px;
  }
  .customers li { display: flex; align-items: flex-start; height: 31px; }
  .customers li.two-line { height: 50px; }
  .customers li.gap { margin-top: 6px; }
  .customers svg { flex: 0 0 20px; margin: 2px 12px 0 0; }

  .desk-photo {
    position: absolute; left: 255px; top: 482px; width: 343px; height: 451px;
    background: radial-gradient(ellipse at 55% 55%, #d7d9dc 0%, #e9e6df 45%, #f2efe8 100%);
  }

  .mark {
    position: absolute; display: flex; flex-direction: column; align-items: center;
    text-align: center;
  }
  .mark .disc { border-radius: 50%; background: radial-gradient(circle at 40% 35%, #b8d43a, var(--green-light) 55%, var(--green) 100%); }
  .mark .name { font-weight: 700; color: var(--green); }
  .mark-small { left: 40px; top: 718px; width: 170px; }
  .mark-small .disc { width: 86px; height: 86px; margin-bottom: 8px; }
  .mark-small .name { font-size: 14px; line-height: 17px; }

  .partners {
    position: absolute; left: 0; top: 880px; width: 598px; height: 53px;
    background: rgba(255,255,255,.82);
    border-top: 2px solid var(--amber);
    display: flex; align-items: center; gap: 16px; padding: 0 20px;
  }
  .partners .label { font-weight: 700; font-size: 13px; color: var(--ink); white-space: nowrap; }
  .partners .partner {
    display: flex; align-items: center; gap: 5px;
    font-size: 13px; font-weight: 700; color: var(--partner-grey); white-space: nowrap;
  }
  .partners .partner::before {
    content: ""; width: 9px; height: 9px; background: var(--partner-grey);
  }

  /* ---------- cover panel (right) ---------- */
  .panel-cover {
    position: absolute; left: 598px; top: 0; width: 602px; height: 933px;
    background: linear-gradient(180deg, #d8dadd 0%, #eeeeee 60%, #e6e6e6 100%);
    border-left: 1px solid #cfcfcf;
  }
  .tile-wall {
    position: absolute; left: 0; top: 0; width: 602px; height: 590px;
    background: radial-gradient(ellipse at 25% 30%, var(--tile-blue) 0%, var(--tile-deep) 35%, rgba(90,160,230,.55) 65%, rgba(220,222,226,0) 88%);
  }
  .headline {
    position: absolute; right: 35px; top: 80px; text-align: right; line-height: 1;
    color: #111;
  }
  .headline .line-a { font-size: 33px; }
  .headline .line-a strong { color: var(--green); }
  .headline .line-b { font-size: 31px; margin-top: 1px; }

  .mark-large { left: 330px; top: 198px; width: 250px; }
  .mark-large .disc { width: 150px; height: 150px; margin-bottom: 12px; }
  .mark-large .name { font-size: 19px; line-height: 22px; }

  .swoosh { position: absolute; left: 0; top: 540px; }

  .services {
    position: absolute; left: 22px; top: 585px;
    font-family: "Roboto Condensed", "Arial Narrow", sans-serif;
    font-size: 35px; line-height: 36px; color: #111;
  }
  .services .it { font-weight: 700; color: var(--green); }

  .team-photo {
    position: absolute; left: 92px; top: 528px; width: 510px; height: 405px;
    background: radial-gradient(ellipse at 50% 55%, #7b7770 0%, #a9a49b 40%, rgba(220,220,220,0) 75%);
  }
</style>
</head>
<body>
<main class="spread">

  <section class="panel-inside">
    <div class="intro-band">
      <span class="brand">BDW</span> has provided service for over 18 years<br>
      Our Enterprise clients as well as to leading<br>
      small / medium business.
    </div>

    <div class="section-label label-offerings">Our company offerings are</div>
    <ul class="offerings">
      <li>Systems integration • IT Support</li>
      <li>Nimbrel - Disaster Recovery solution -</li>
      <li class="note">Nimbrel Information is in a attached document</li>
      <li>Harbor Sky Suite - Hosted Mailvane and Cloud Servers</li>
      <li>N.O.C. Managed Services</li>
      <li>Around-the-clock network surveillance</li>
      <li>Performance monitoring</li>
      <li>Trouble ticket management</li>
      <li>Event management</li>
      <li>Guaranteed service levels (service assurance)</li>
    </ul>

    <div class="desk-photo" role="img" aria-label="Photo of a desk with a flat-screen computer, keyboard and desk lamp"></div>

    <div class="section-label label-customers">Some of our customer includes:</div>
    <ul class="customers">
      <li><svg width="20" height="18" viewBox="0 0 20 18"><rect x="1" y="3" width="14" height="14" fill="#fff" stroke="var(--check-blue)" stroke-width="2"/><path d="M4 9l4 4 10-11" fill="none" stroke="var(--check-blue)" stroke-width="3"/></svg>Healthcare</li>
      <li><svg width="20" height="18" viewBox="0 0 20 18"><rect x="1" y="3" width="14" height="14" fill="#fff" stroke="var(--check-blue)" stroke-width="2"/><path d="M4 9l4 4 10-11" fill="none" stroke="var(--check-blue)" stroke-width="3"/></svg>Government</li>
      <li><svg width="20" height="18" viewBox="0 0 20 18"><rect x="1" y="3" width="14" height="14" fill="#fff" stroke="var(--check-blue)" stroke-width="2"/><path d="M4 9l4 4 10-11" fill="none" stroke="var(--check-blue)" stroke-width="3"/></svg>Educational Institutions</li>
      <li><svg width="20" height="18" viewBox="0 0 20 18"><rect x="1" y="3" width="14" height="14" fill="#fff" stroke="var(--check-blue)" stroke-width="2"/><path d="M4 9l4 4 10-11" fill="none" stroke="var(--check-blue)" stroke-width="3"/></svg>Banking &amp; Insurance companies</li>
      <li class="two-line"><svg width="20" height="18" viewBox="0 0 20 18"><rect x="1" y="3" width="14" height="14" fill="#fff" stroke="var(--check-blue)" stroke-width="2"/><path d="M4 9l4 4 10-11" fill="none" stroke="var(--check-blue)" stroke-width="3"/></svg><span>Pharmaceutical, Bio-Technology<br>and Medical Devices companies</span></li>
      <li class="gap"><svg width="20" height="18" viewBox="0 0 20 18"><rect x="1" y="3" width="14" height="14" fill="#fff" stroke="var(--check-blue)" stroke-width="2"/><path d="M4 9l4 4 10-11" fill="none" stroke="var(--check-blue)" stroke-width="3"/></svg>Manufacturing and Regulatory Organizations</li>
      <li><svg width="20" height="18" viewBox="0 0 20 18"><rect x="1" y="3" width="14" height="14" fill="#fff" stroke="var(--check-blue)" stroke-width="2"/><path d="M4 9l4 4 10-11" fill="none" stroke="var(--check-blue)" stroke-width="3"/></svg>Many others</li>
    </ul>

    <div class="mark mark-small">
      <div class="disc"></div>
      <div class="name">Brightmoor Data Works Inc.</div>
    </div>

    <div class="partners">
      <span class="label">Our partners:</span>
      <span class="partner">Veltro</span>
      <span class="partner">Dranwell</span>
      <span class="partner">QZR</span>
      <span class="partner">Palvo</span>
      <span class="partner">Membrix</span>
      <span class="partner">XVL</span>
    </div>
  </section>

  <section class="panel-cover">
    <div class="tile-wall" role="img" aria-label="Illustration of a curved wall of glossy blue tiles over a faint world map"></div>

    <div class="headline">
      <div class="line-a">A <strong>World Class</strong></div>
      <div class="line-b">service with you in mind</div>
    </div>

    <div class="mark mark-large">
      <div class="disc"></div>
      <div class="name">Brightmoor Data Works Inc.</div>
    </div>

    <svg class="swoosh" width="602" height="260" viewBox="0 0 602 260" aria-hidden="true">
      <path d="M0 150 C150 60 380 10 602 30 L602 62 C400 50 170 110 0 245 Z" fill="var(--amber)" opacity=".9"/>
      <path d="M0 245 C170 110 400 50 602 62 L602 72 C400 62 180 120 0 260 Z" fill="#fff" opacity=".8"/>
    </svg>

    <div class="team-photo" role="img" aria-label="Photo of three business professionals around a laptop"></div>

    <div class="services">
      Consulting<br>Services<br>and <span class="it">IT</span> Staffing<br>Support
    </div>
  </section>

</main>
</body>
</html>
```